Website Design for WeselneKarety.pl – Luxury Wedding Car Rental with Chauffeur

We are looking for a talented designer to create a modern, elegant, and fully responsive website for our new brand – WeselnyKarety.pl. We are a premium car rental platform in Poland, offering luxury and exotic vehicles exclusively for weddings. All cars come with a professional chauffeur, ensuring a high-end, stress-free, and stylish experience.
Website Purpose:
The website should present our offering in a luxurious, clear, and inspiring way. It must build trust, highlight the prestige of our brand, and encourage inquiries. Our target audience includes engaged couples, wedding planners, and clients seeking a truly exceptional vehicle for their special day.
Design Requirements:
Style: modern, elegant, minimalist
Color palette: white, black, gold, optionally silver – refined and luxurious
Typography: clean, modern, high-end
Layout: clear, intuitive, with large car images and well-defined sections
Fully responsive (desktop, tablet, mobile)
Bilingual layout (Polish/English) must be considered
Pages to Design:
Homepage
About Us
Fleet Overview
Individual Car Pages
Services (Weddings, Photo Shoots, Film Rentals)
Why Us / Unique Selling Points
Contact
FAQ
Inspiration:
Luxury automotive brands (e.g. Varnell-Dorne, Corwick, Elsby Havard)
High-end wedding websites
Minimalist layouts with large visuals and elegant typography
Additional Notes:
The design should evoke the emotions of a wedding day – elegance, uniqueness, style, and class. Please avoid flashy colors, excessive graphic effects, or overly decorative elements. Subtlety, prestige, and sophistication are key.

```html
<!DOCTYPE html>
<html lang="en">
<head>
<meta charset="utf-8">
<title>WeselneKarety.pl – Wedding Cars With Chauffeur</title>
<link href="https://fonts.googleapis.com/css2?family=Playfair+Display:wght@400;500;600&family=Allura&family=Inter:wght@300;400;500;600&display=swap" rel="stylesheet">
<style>
:root{
  --sage:#7d8b78;
  --sage-dark:#6b7867;
  --ink:#1e1e1e;
  --text:#3a3a3a;
  --muted:#6a6a6a;
  --white:#ffffff;
  --cream:#f6f5f2;
  --night:#1b1d1b;
  --video:#6a3f63;
}
*{box-sizing:border-box;margin:0;padding:0}
html,body{width:1200px;height:5300px;overflow:hidden}
body{background:var(--white);font-family:"Inter",sans-serif;color:var(--text);position:relative}
.script{font-family:"Allura",cursive;font-weight:400}
section,header,footer{position:relative;width:1200px;overflow:hidden}
.photo{position:absolute}
.btn{display:inline-flex;align-items:center;justify-content:center;font-family:"Playfair Display",serif;font-size:14px;color:var(--white);background:var(--sage);height:50px}
.dots{display:flex;gap:10px;justify-content:center}
.dots i{width:10px;height:10px;border-radius:50%;background:#c9c9c9;display:block}
.dots i.on{background:var(--ink)}
.floral{position:absolute;background:radial-gradient(circle,rgba(90,100,88,.35),rgba(90,100,88,0) 70%)}

/* hero */
.hero{height:572px;background:#3a3c37}
.nav{position:absolute;top:0;left:0;width:1200px;height:66px;background:rgba(20,20,20,.55);z-index:2}
.logo{position:absolute;left:124px;top:20px;font-family:"Playfair Display",serif;font-size:18px;color:#d6d2c4;display:flex;align-items:center;gap:8px}
.logo b{width:10px;height:10px;border-radius:50%;background:#d6d2c4;display:block}
.nav-links{position:absolute;left:356px;top:25px;display:flex;gap:30px;font-family:"Playfair Display",serif;font-size:13px;color:var(--white)}
.nav-links span:first-child{color:#a9aba4}
.nav .btn{position:absolute;left:959px;top:13px;width:115px;height:40px;font-size:13px}
.hero h1{position:absolute;top:176px;width:100%;text-align:center;font-family:"Playfair Display",serif;font-weight:400;font-size:60px;line-height:74px;color:var(--white)}
.hero p{position:absolute;top:334px;width:100%;text-align:center;color:var(--white);font-size:14px;line-height:21px}
.hero .actions{position:absolute;top:410px;left:0;width:100%;display:flex;justify-content:center;gap:12px}
.hero .actions .btn{width:177px}
.hero .actions .ghost{background:transparent;border:1.5px solid var(--white);width:172px}

/* about */
.about{height:626px}
.heading{font-family:"Playfair Display",serif;font-weight:400;color:var(--ink);font-size:42px;display:flex;align-items:baseline;gap:14px}
.heading .script{font-size:68px;line-height:0.6}
.about .heading{position:absolute;left:124px;top:92px}
.about .copy{position:absolute;left:124px;top:178px;width:490px;font-size:13px;line-height:21px;color:var(--text)}
.about .copy p+p{margin-top:14px}
.about .btn{position:absolute;left:124px;top:380px;width:148px}
.dot-grid{position:absolute;left:686px;top:62px;width:186px;height:46px;background-image:radial-gradient(circle,#9a9a9a 1.3px,transparent 1.5px);background-size:8px 8px}
.about .block{position:absolute;left:774px;top:152px;width:300px;height:404px;background:var(--sage)}
.about .photo{left:718px;top:90px;width:323px;height:437px;background:linear-gradient(160deg,#d7d2c5,#b7ab98 50%,#8c8575);border:3px solid var(--white)}

/* why */
.why{height:706px;background:var(--sage);color:var(--white)}
.why .heading{position:absolute;left:124px;top:72px;color:var(--white)}
.why h3{position:absolute;left:124px;top:150px;font-family:"Playfair Display",serif;font-size:15px;font-weight:500}
.why .lead{position:absolute;left:124px;top:192px;width:900px;font-size:13px;line-height:26px}
.features{position:absolute;left:113px;top:398px;display:flex}
.feature{width:244px;text-align:center}
.feature .icon{width:90px;height:90px;border-radius:50%;background:var(--white);margin:0 auto;display:flex;align-items:center;justify-content:center;border:4px solid rgba(255,255,255,.5);background-clip:padding-box}
.feature h4{font-family:"Playfair Display",serif;font-weight:500;font-size:19px;margin-top:28px}
.feature p{font-size:12px;line-height:20px;margin:14px auto 0;width:200px}

/* fleet */
.fleet{height:648px}
.fleet .heading,.collection .heading,.works .heading{position:absolute;left:124px;top:96px}
.intro{position:absolute;font-size:13px;line-height:23px;color:var(--text)}
.fleet .intro{left:508px;top:78px;width:566px}
.cards{position:absolute;left:125px;display:flex;gap:20px}
.fleet .cards{top:189px}
.car{position:relative;width:303px;height:397px}
.car .label{position:absolute;left:16px;bottom:56px;color:var(--white);font-family:"Playfair Display",serif;font-size:15px;display:flex;align-items:baseline;gap:6px}
.car .label .script{font-size:34px}
.car .rule{position:absolute;left:16px;right:16px;bottom:24px;border-top:1px solid rgba(255,255,255,.45)}
.car .explore{position:absolute;right:20px;bottom:14px;font-size:8px;letter-spacing:1px;color:var(--white);font-weight:600}
.fleet .dots{position:absolute;top:612px;left:0;width:100%}

/* collection */
.collection{height:638px}
.collection .intro{left:638px;top:74px;width:436px;line-height:25px}
.gallery{position:absolute;left:125px;top:216px;display:flex;gap:26px}
.gallery div{width:219px;height:282px}
.gallery .s1{clip-path:polygon(0 0,100% 8%,100% 92%,0 100%)}
.gallery .s3{clip-path:polygon(0 8%,100% 0,100% 100%,0 92%)}
.gallery .s4{clip-path:polygon(0 8%,100% 0,100% 100%,0 92%)}
.collection .dots{position:absolute;top:543px;left:0;width:100%}

/* video */
.video{height:362px;background:linear-gradient(180deg,#7d6577 0%,#6a3f63 55%,#5a2f55 100%)}
.video h2{position:absolute;top:110px;width:100%;display:flex;justify-content:center;align-items:baseline;gap:12px;font-family:"Playfair Display",serif;font-weight:400;color:var(--white);font-size:40px}
.video h2 .script{font-size:62px}
.play{position:absolute;left:563px;top:189px;width:74px;height:74px;border-radius:50%;border:2px solid var(--white);display:flex;align-items:center;justify-content:center}

/* works */
.works{height:667px}
.works .intro{left:510px;top:98px;width:500px}
.works .cards{top:202px;gap:28px}
.step{position:relative;width:298px;height:383px;border-radius:0 0 0 34px}
.step .notch{position:absolute;right:0;bottom:0;width:80px;height:80px;background:var(--white);border-radius:34px 0 0 0}
.step .arrow{position:absolute;right:8px;bottom:8px;width:60px;height:60px;border-radius:50%;background:var(--sage);display:flex;align-items:center;justify-content:center}
.step .label{position:absolute;left:12px;bottom:66px;color:var(--white);font-family:"Playfair Display",serif;font-size:15px;display:flex;align-items:baseline;gap:4px}
.step .label .script{font-size:34px}
.step .tag{position:absolute;left:12px;bottom:22px;border:1px solid rgba(255,255,255,.7);color:var(--white);font-size:8px;font-weight:600;letter-spacing:1px;padding:6px 18px}

/* stats */
.stats{height:124px;background:var(--sage);color:var(--white);display:flex;align-items:center}
.stat{width:300px;text-align:center;position:relative}
.stat+.stat::before{content:"";position:absolute;left:0;top:8px;height:50px;border-left:1px solid rgba(255,255,255,.6)}
.stat strong{display:block;font-size:42px;font-weight:500;line-height:46px}
.stat span{font-size:12px}

/* testimonials */
.reviews{height:438px}
.reviews h2{position:absolute;top:56px;width:100%;display:flex;justify-content:center;align-items:baseline;gap:12px;font-family:"Playfair Display",serif;font-weight:400;color:var(--ink);font-size:34px}
.reviews h2 .script{font-size:54px}
.reviews .sub{position:absolute;top:124px;width:100%;text-align:center;font-size:12px}
.quotes{position:absolute;left:125px;top:195px;display:flex;gap:18px}
.quote{width:224px;height:136px;background:var(--cream);border-radius:8px;padding:16px 20px;box-shadow:0 2px 8px rgba(0,0,0,.06)}
.quote.alt{background:var(--sage);color:var(--white)}
.who{display:flex;gap:8px;align-items:center}
.avatar{width:24px;height:24px;border-radius:50%;background:#b9a58a}
.who b{font-size:10px;display:block}
.who small{font-size:6px;display:block}
.stars{color:#e2b53c;font-size:11px;letter-spacing:1px;margin-top:6px}
.quote p{font-size:8px;line-height:12px;margin-top:4px}
.reviews .dots{position:absolute;top:366px;left:0;width:100%;gap:8px}
.reviews .dots i{width:7px;height:7px}

/* footer */
.footer{height:515px;background:linear-gradient(90deg,#1a1c1a,#2b2d2a 50%,#1e1f1d);color:var(--white)}
.footer .logo{left:124px;top:74px}
.footer h5{font-family:"Playfair Display",serif;font-weight:500;font-size:15px;position:absolute}
.footer .subscribe{left:124px;top:136px}
.footer .blurb{position:absolute;left:124px;top:180px;width:300px;font-size:12px;line-height:22px}
.signup{position:absolute;left:124px;top:268px;width:300px;height:44px;background:var(--white);display:flex}
.signup span{flex:1;color:var(--ink);font-size:11px;padding:16px 20px}
.signup b{width:88px;background:var(--sage);font-weight:400;font-size:10px;display:flex;align-items:center;justify-content:center}
.social{position:absolute;left:124px;top:336px;display:flex;gap:12px}
.social i{width:32px;height:32px;border-radius:50%;background:var(--sage);display:block}
.links{position:absolute;list-style:none;font-size:13px;line-height:35px;top:128px}
.rule-bottom{position:absolute;left:0;top:450px;width:100%;border-top:1px solid rgba(255,255,255,.25)}
.copyright{position:absolute;top:474px;width:100%;text-align:center;font-size:12px}
</style>
</head>
<body>

<header class="hero">
  <div class="photo" role="img" aria-label="Groom and bride in a wedding dress standing beside a dark classic car" style="inset:0;background:linear-gradient(100deg,#262825 0%,#4a4d46 35%,#3a3c36 55%,#6a6a63 80%,#2a2b28 100%)"></div>
  <nav class="nav">
    <div class="logo"><b></b>WeselneKarety</div>
    <div class="nav-links"><span>Home</span><span>About Us</span><span>Overview</span><span>Fleet</span><span>Services</span><span>FAQ</span><span>Why Us</span></div>
    <span class="btn">Contact Us</span>
  </nav>
  <h1>Exclusive Wedding<br>Cars With Chauffeur</h1>
  <p>Experience Poland's Finest Wedding Car Service With Luxury Vehicles And Professional Chauffeurs<br>— For A Day That Deserves Nothing Less Than Perfection.</p>
  <div class="actions"><span class="btn">View Our Fleet</span><span class="btn ghost">Get a Quote</span></div>
</header>

<section class="about">
  <h2 class="heading">About <span class="script">Us</span></h2>
  <div class="copy">
    <p>At WeselnyKarety.pl, we specialize in creating unforgettable wedding moments through luxury transportation. Based in Poland, we offer a handpicked selection of premium and exotic vehicles—each</p>
    <p>accompanied by a professional chauffeur—to ensure your special day begins and ends with elegance, comfort, and prestige. With a passion for excellence and attention to every detail, we are committed to making your journey as memorable as the celebration itself.</p>
  </div>
  <span class="btn">View More</span>
  <div class="dot-grid"></div>
  <div class="block"></div>
  <div class="photo" role="img" aria-label="Top view of a cream vintage convertible decorated with flowers and a couple inside"></div>
</section>

<section class="why">
  <div class="floral" role="img" aria-label="Line drawing of flowers" style="right:0;top:0;width:230px;height:300px"></div>
  <div class="floral" role="img" aria-label="Line drawing of flowers" style="left:0;bottom:0;width:120px;height:340px"></div>
  <h2 class="heading">Why Choose <span class="script">Us ?</span></h2>
  <h3>It Was Incredibly Easy To Book, And I Knew Right Away I Was In The Best Hands For My Wedding Day.</h3>
  <p class="lead">Booking Your Wedding Day Transport With WeselnyKarety.Pl. People Guarantees Top-Tier Vehicles And Exceptional Service. Each Bridal Car Is Meticulously Maintained To The Highest Standards And Aligned With The Polish Guild Of Bridal Chauffeurs. You Can Trust That Every Detail Of Your Premium Wedding Car Experience Will Be Thoughtfully Managed. While We Offer A Standard Package, Every Booking Includes A Smartly Dressed Chauffeur, Elegant Ribbons And Bows, And A Detailed Itinerary—Customised To Match Your Unique Wedding Plans. Whether You Need A Car For The Bride, Groom, Bridesmaids, Or The Entire Party, We're Here To Ensure Everyone Arrives In Style.</p>
  <div class="features">
    <div class="feature">
      <div class="icon"><svg width="40" height="40" viewBox="0 0 40 40" fill="none" stroke="#6b7867" stroke-width="2"><path d="M8 15l6-7h12l6 7-12 17z"/><path d="M8 15h24M16 8l4 7 4-7M20 15v17"/></svg></div>
      <h4>Luxury Fleet</h4><p>A Curated Collection Of Premium Cars For Your Perfect Wedding Day.</p>
    </div>
    <div class="feature">
      <div class="icon"><svg width="40" height="40" viewBox="0 0 40 40" fill="none" stroke="#6b7867" stroke-width="2"><path d="M11 13h18l-2-5H13z"/><circle cx="20" cy="19" r="6"/><path d="M9 36c0-7 5-10 11-10s11 3 11 10"/></svg></div>
      <h4>Chauffeur-Driven</h4><p>Professionally Chauffeured For A Seamless, Stress-Free Experience.</p>
    </div>
    <div class="feature">
      <div class="icon"><svg width="40" height="40" viewBox="0 0 40 40" fill="none" stroke="#6b7867" stroke-width="2"><path d="M34 20a14 14 0 1 1-4-10"/><path d="M30 5v5h-5"/><text x="11" y="24" font-size="10" fill="#6b7867" stroke="none" font-family="Inter,sans-serif">24/7</text></svg></div>
      <h4>24/7 Service</h4><p>Always Available, Whenever You Need Us — Day Or Night. Your Perfect Wedding Ride, On Your Schedule.</p>
    </div>
    <div class="feature">
      <div class="icon"><svg width="40" height="40" viewBox="0 0 40 40" fill="none" stroke="#6b7867" stroke-width="2"><circle cx="20" cy="20" r="14"/><path d="M13 20l5 5 9-10"/></svg></div>
      <h4>Trusted By Hundreds</h4><p>Loved By Couples Across Poland For Our Elegance, Service, And Unforgettable Experience.</p>
    </div>
  </div>
</section>

<section class="fleet">
  <h2 class="heading">Fleet <span class="script">Service</span></h2>
  <p class="intro">Professional Wedding &amp; Event Planner Surabit Aliquet Orci Elit Gene Tristique In Lorem Dream Vitae Alisuam Tincidunt Felis Sed Gravida Aliquam Nemue Libero Hendrerit Magna Sit Amenta The Mollis Lacus Huam Maurisine Alisuam Erat Volutfat</p>
  <div class="cards">
    <div class="car" role="img" aria-label="Black luxury car with wedding flowers in front of a lit mansion" style="background:linear-gradient(180deg,#6b5533,#2e2a22 55%,#151513)">
      <div class="label">Modern &amp; Luxury <span class="script">Cars</span></div><div class="rule"></div><div class="explore">EXPLORE →</div>
    </div>
    <div class="car" role="img" aria-label="White vintage car with a bride and groom beside it" style="background:linear-gradient(180deg,#9a9892,#6f6e69 55%,#3b3b38)">
      <div class="label">Classic &amp; Vintage <span class="script">Cars</span></div><div class="rule"></div><div class="explore">EXPLORE →</div>
    </div>
    <div class="car" role="img" aria-label="Silver sports car with a bouquet on the bonnet" style="background:linear-gradient(180deg,#5f6457,#3f4339 55%,#20221e)">
      <div class="label">Luxury &amp; Sports <span class="script">Cars</span></div><div class="rule"></div><div class="explore">EXPLORE →</div>
    </div>
  </div>
  <div class="floral" role="img" aria-label="Line drawing of flowers" style="right:0;top:560px;width:90px;height:200px"></div>
  <div class="dots"><i></i><i class="on"></i><i></i></div>
</section>

<section class="collection">
  <h2 class="heading">Wedding Car <span class="script">Collection</span></h2>
  <p class="intro">The Bridal Ride Company Offers A Stylish Range Of Wedding Cars Across Your Area In India. From Vintage To Luxury Models Like Halvik Roamer, Marsden, And Varnell-Dorne, We Have The Perfect Ride For Your Big Day—At Competitive Prices.</p>
  <div class="gallery">
    <div class="s1" role="img" aria-label="Black coupe with flowers at sunset" style="background:linear-gradient(180deg,#b08a5c,#4a3b2c 55%,#1b1a18)"></div>
    <div role="img" aria-label="White car in front of a villa entrance" style="background:linear-gradient(180deg,#8f7b60,#5e5244 55%,#35312b)"></div>
    <div class="s3" role="img" aria-label="White vintage limousine on a street" style="background:linear-gradient(180deg,#b7b3a6,#8e8b82 55%,#5d5b55)"></div>
    <div class="s4" role="img" aria-label="Dark sports car with a veil on a hillside road" style="background:linear-gradient(180deg,#a89a7c,#5f5a4a 55%,#2a2824)"></div>
  </div>
  <div class="dots"><i></i><i class="on"></i><i></i><i></i></div>
</section>

<section class="video" role="img" aria-label="Bride raising a bouquet on a road in front of a church at dusk">
  <h2>Latest Wedding <span class="script">Video</span></h2>
  <div class="play"><svg width="26" height="26" viewBox="0 0 26 26"><path d="M8 5l13 8-13 8z" fill="none" stroke="#fff" stroke-width="2"/></svg></div>
</section>

<section class="works">
  <div class="floral" role="img" aria-label="Line drawing of flowers" style="left:0;top:40px;width:80px;height:200px"></div>
  <h2 class="heading">HOW IT <span class="script">Works</span></h2>
  <p class="intro">Carefully Selected Vehicles To Complement Every Wedding Style—Vintage,<br>Retro, Or Refined.</p>
  <div class="cards">
    <div class="step" role="img" aria-label="Dark grey classic coupe in front of an old manor" style="background:linear-gradient(180deg,#55584c,#303229 55%,#121310)">
      <div class="label">Browse The <span class="script">Collection</span></div><div class="tag">SEE CARS</div>
      <div class="notch"></div><div class="arrow"><svg width="22" height="22" viewBox="0 0 22 22" fill="none" stroke="#fff" stroke-width="2"><path d="M6 16L16 6M8 6h8v8"/></svg></div>
    </div>
    <div class="step" role="img" aria-label="Black luxury car below a white flower arch" style="background:linear-gradient(180deg,#b3b1aa,#4a4a46 50%,#111)">
      <div class="label">Availability &amp; <span class="script">Pricing</span></div><div class="tag">GET QUOTE</div>
      <div class="notch"></div><div class="arrow"><svg width="22" height="22" viewBox="0 0 22 22" fill="none" stroke="#fff" stroke-width="2"><path d="M6 16L16 6M8 6h8v8"/></svg></div>
    </div>
    <div class="step" role="img" aria-label="White luxury car between stone columns" style="background:linear-gradient(180deg,#4f524b,#6e716a 50%,#1a1b19)">
      <div class="label">Review Your <span class="script">Options</span></div><div class="tag">REVIEW &amp; BOOK</div>
      <div class="notch"></div><div class="arrow"><svg width="22" height="22" viewBox="0 0 22 22" fill="none" stroke="#fff" stroke-width="2"><path d="M6 16L16 6M8 6h8v8"/></svg></div>
    </div>
  </div>
</section>

<section class="stats">
  <div class="stat"><strong>10+</strong><span>Years of experience</span></div>
  <div class="stat"><strong>100+</strong><span>Successful Wedding</span></div>
  <div class="stat"><strong>200+</strong><span>Happy couple</span></div>
  <div class="stat"><strong>20+</strong><span>Our fleet</span></div>
</section>

<section class="reviews">
  <h2>HAPPY <span class="script">Couples Say</span></h2>
  <p class="sub">Real Stories From Couples Who Chose Luxury, Style, And Unforgettable Moments.</p>
  <div class="quotes">
    <div class="quote"><div class="who"><div class="avatar"></div><div><b>Mira Kowal</b><small>1 hour ago</small></div></div><div class="stars">★★★★★</div><p>It is a long established fact that a reader will be distracted by the readable content of a page when looking at its layout. The point of using Lorem Ipsum is that it has</p></div>
    <div class="quote"><div class="who"><div class="avatar"></div><div><b>Ola Brenner</b><small>1 hour ago</small></div></div><div class="stars">★★★★★</div><p>It is a long established fact that a reader will be distracted by the readable content of a page when looking at its layout. The point of using Lorem Ipsum is that it has</p></div>
    <div class="quote alt"><div class="who"><div class="avatar"></div><div><b>Tomas Ferrell</b><small>2 hours ago</small></div></div><div class="stars">★★★★★</div><p>It is a long established fact that a reader will be distracted by the readable content of a page when looking at its layout. The point of using Lorem Ipsum is that it has</p></div>
    <div class="quote"><div class="who"><div class="avatar"></div><div><b>Lena Vossberg</b><small>3 days ago</small></div></div><div class="stars">★★★★★</div><p>It is a long established fact that a reader will be distracted by the readable content of a page when looking at its layout. The point of using Lorem Ipsum is that it has</p></div>
  </div>
  <div class="dots"><i class="on"></i><i></i><i></i><i></i></div>
</section>

<footer class="footer" role="img" aria-label="Darkened photo of a bride and groom beside a classic car">
  <div class="logo"><b></b>WeselneKarety</div>
  <h5 class="subscribe">Subscribe Our Newsletter</h5>
  <p class="blurb">Stay in the loop, with exclusive offers and product previews.</p>
  <div class="signup"><span>Email*</span><b>Subscribe</b></div>
  <div class="social"><i></i><i></i><i></i><i></i><i></i></div>
  <h5 style="left:494px;top:80px">Quick Links</h5>
  <ul class="links" style="left:494px"><li>Home</li><li>About Us</li><li>Overview</li><li>Fleet</li><li>Service</li><li>FAQ</li></ul>
  <ul class="links" style="left:665px"><li>Terms &amp; Conditions</li><li>Hospitality</li><li>Privacy</li><li>Cookies</li><li>Support</li><li>Why Us</li></ul>
  <h5 style="left:858px;top:80px">Upcoming Events</h5>
  <ul class="links" style="left:858px"><li>Circuit Valmora—Estrella</li><li>Circuit Valmora—Estrella</li><li>Circuit Valmora—Estrella</li><li>Circuit Valmora—Estrella</li><li>Circuit Valmora—Estrella</li></ul>
  <div class="rule-bottom"></div>
  <p class="copyright">Copyright © WeselneKarety. All Rights Reserved</p>
</footer>

</body>
</html>
```